Web Design - Personal Item Tags Portal

web page designs need to be created for a new company that provides item tracking tags and lets users register and report stolen/found items.
The theme of the designs needs to be energetic and convey a sense of freedom and adventure - where the user does not have to worry about their items since they have all been "tagged".
the client likes parts of the site at: http://www.brisklayouts.example/
they like:
1. slider images at top of pages. large slider on front page. fixed smaller height picture on internal pages
2. fixed company message on left-hand-side
3. My Account button to be clear and stand out

other comments:
clean, simple
• brand focused
• will have clear call to actions
• will include a description of what and why
• will appeal to both males and females

sections that the website will have are:
Home
About Us
How it works
Why
Case Studies
Uses and Applications
Shop
Contact Us

please create 2 designs : 1 home page, 1 internal page

Final winner will also require HTML slicing to be done.
Updates

hi, i have now updated the images so they work. sorry!

Hi, looking at all the designs that are coming in, alot of them are great. Designers need to remember to make the register for an account button more prominent. Also, there should be a "report found" and "report lost" buttons on the front-page and should be prominent as well.

Thanks

Hi, the customer has come back with a few comments and modifications for the designs, if you are able to make some tweaks to your submissions, that will be great:

The client would like the designs to be modified to highlight 3 main actions:
1. Log In/Register
2. Find an Owner
3. Lost an Item

The home page shouldnt be too content heavy in terms of text, it should only have major highlight points of what the system does (the 3 points listed above). the inner page designs are OK to have more text though.

i will also upload some notes from the customer that can be used as a guide and also include the design styles which the customer likes (but is not entirely happy with).

uploaded image files (3) with customer feedback comments

Industry/Entity Type

It Company

```html
<!DOCTYPE html>
<html lang="en">
<head>
<meta charset="utf-8">
<title>TagRoam – How it works</title>
<link rel="stylesheet" href="https://fonts.googleapis.com/css2?family=Arimo:wght@400;700&display=swap">
<style>
:root{
  --black:#000;
  --brand-blue:#1a7fb3;
  --nav-blue:#2aa0dc;
  --heading-blue:#126aa0;
  --button-blue:#1676a8;
  --button-dark:#0f3c5b;
  --text:#000;
  --white:#fff;
  --tick:#5cb82e;
  --social-red:#d34836;
  --social-sky:#4aa8e0;
  --social-tube:#c4302b;
  --social-navy:#3b5998;
}
*{box-sizing:border-box;margin:0;padding:0}
html,body{width:1200px;height:984px;overflow:hidden;background:var(--white)}
body{position:relative;font-family:"Arimo",Arial,sans-serif;color:var(--text)}
.site-header{position:absolute;left:0;top:0;width:1200px;height:114px;background:var(--black)}
.brand{position:absolute;left:138px;top:0;width:376px;height:114px;background:linear-gradient(90deg,#111 0%,#1b1b1b 100%);overflow:hidden}
.brand-glow{position:absolute;left:10px;top:-10px;width:120px;height:120px;border-radius:50%;background:radial-gradient(circle,#3a8fd0 0%,#154b78 40%,rgba(0,0,0,0) 70%)}
.brand-mark{position:absolute;left:46px;top:28px;width:46px;height:46px;border-radius:50%;background:var(--black)}
.brand-name{position:absolute;left:136px;top:6px;font-size:38px;font-weight:700;color:var(--white);letter-spacing:1px}
.brand-tagline{position:absolute;left:140px;top:58px;font-size:16px;font-weight:700;color:var(--white)}
.main-nav{position:absolute;top:55px;left:0;width:1200px;height:24px}
.main-nav a{position:absolute;top:0;font-size:14px;font-weight:700;color:var(--white);text-decoration:none;line-height:24px;white-space:nowrap}
.main-nav a.is-current{color:var(--nav-blue)}
.main-nav a.account{background:var(--brand-blue);border-radius:6px;padding:0 9px 0 27px;height:24px;width:113px}
.account-lock{position:absolute;left:8px;top:4px}
.nav-rule{position:absolute;left:514px;top:86px;width:518px;height:3px;background:#14557f}
.hero{position:absolute;left:0;top:114px;width:1200px;height:540px}
.hero-title,.hero-sub{position:absolute;font-weight:700;line-height:1;white-space:nowrap;text-shadow:0 0 2px #0b3550,1px 1px 2px #0b3550,-1px -1px 2px #0b3550}
.hero-title{left:578px;top:70px;font-size:37.5px;color:#6fc4f0}
.hero-sub{left:581px;top:106px;font-size:29px;color:#8dd2f5;letter-spacing:1px}
.help-panel{position:absolute;left:154px;top:370px;width:284px;height:230px;background:var(--white);box-shadow:0 0 8px rgba(0,0,0,.25);padding:26px 10px 0 30px}
.help-panel h2{font-size:20px;font-weight:700;color:var(--heading-blue);text-align:center;margin-left:-20px;line-height:1}
.help-panel p{font-size:18px;line-height:18.7px;margin-top:10px;white-space:nowrap}
.help-panel p + p{margin-top:18.7px}
.cta{position:absolute;left:190px;width:211px;height:52px;border-radius:26px;background:linear-gradient(#1f86bd,var(--button-blue));box-shadow:0 5px 5px rgba(0,0,0,.3);color:var(--white);text-decoration:none;display:flex;align-items:center;white-space:nowrap}
.cta-icon{position:absolute;right:11px;top:9px;width:34px;height:34px;border-radius:50%;background:var(--button-dark);display:flex;align-items:center;justify-content:center}
.cta-register{top:622px;font-size:17px;padding-left:21px}
.cta-contact{top:713px;font-size:22px;padding-left:36px}
.cta-subscribe{top:778px;font-size:17px;line-height:18px;padding-left:28px}
.content{position:absolute;left:467px;top:406px;width:600px}
.content h1{font-size:24px;font-weight:700;color:var(--heading-blue);line-height:24px;margin-bottom:8px}
.content p{font-size:15px;line-height:15px;margin-bottom:7px;white-space:nowrap}
.checklist{list-style:none;margin:16px 0 27px 3px}
.checklist li{font-size:15px;line-height:15px;padding-left:24px;position:relative;white-space:nowrap}
.checklist svg{position:absolute;left:0;top:0}
.site-footer{position:absolute;left:0;top:882px;width:1200px;height:102px;background:var(--black);color:var(--white)}
.footer-links{position:absolute;left:151px;top:30px;font-size:15.5px;line-height:16px;white-space:nowrap}
.footer-links a{color:var(--white);text-decoration:none}
.footer-links .sep{margin:0 9px}
.social{position:absolute;top:28px;width:35px;height:35px;border:1px solid #777}
</style>
</head>
<body>
<header class="site-header">
  <div class="brand">
    <div class="brand-glow"></div>
    <div class="brand-mark"></div>
    <div class="brand-name">TagRoam</div>
    <div class="brand-tagline">. . . adventure first</div>
  </div>
  <nav class="main-nav">
    <a href="#" style="left:448px">About</a>
    <a href="#" class="is-current" style="left:504px">How it works</a>
    <a href="#" style="left:612px">Case Studies</a>
    <a href="#" style="left:714px">Applications</a>
    <a href="#" style="left:809px">Shop</a>
    <a href="#" class="account" style="left:854px">
      <svg class="account-lock" width="14" height="15" viewBox="0 0 14 15"><path d="M3.5 7V4.5a3.5 3.5 0 0 1 7 0V7" fill="none" stroke="#fff" stroke-width="2"/><rect x="1" y="7" width="12" height="8" rx="1" fill="#fff"/></svg>My account</a>
    <a href="#" style="left:982px">Contact</a>
  </nav>
  <div class="nav-rule"></div>
</header>

<section class="hero">
  <svg width="1200" height="540" viewBox="0 0 1200 540">
    <defs>
      <linearGradient id="heroTones" x1="0" y1="0" x2="1" y2="0">
        <stop offset="0" stop-color="#5d7a70"/>
        <stop offset=".3" stop-color="#7e8f8a"/>
        <stop offset=".45" stop-color="#2c2c30"/>
        <stop offset=".7" stop-color="#6b6b6b"/>
        <stop offset="1" stop-color="#8a8a88"/>
      </linearGradient>
    </defs>
    <rect role="img" aria-label="Photo of a climber scaling a grey rock face above a forested valley" width="1200" height="540" fill="url(#heroTones)"/>
    <path d="M0 426 C250 290 500 228 700 230 C900 232 1100 245 1200 252 L1200 540 L0 540Z" fill="#fff"/>
  </svg>
  <div class="hero-title">Freedom and Adventure</div>
  <div class="hero-sub">don't worry about your items</div>
</section>

<aside class="help-panel">
  <h2>How We Can Help You</h2>
  <p>We provide item tracking<br>tags and lets users register<br>and report stolen/found<br>items.</p>
  <p>You do not have to worry<br>about your items since<br>they have all been<br>"tagged".</p>
</aside>

<a href="#" class="cta cta-register">REGISTER NOW
  <span class="cta-icon"><svg width="18" height="16" viewBox="0 0 18 16"><path d="M1 5h8V1l8 7-8 7v-4H1z" fill="#fff"/></svg></span></a>
<a href="#" class="cta cta-contact">Contact Us
  <span class="cta-icon"><svg width="20" height="18" viewBox="0 0 20 18"><ellipse cx="8" cy="7" rx="7" ry="5.5" fill="#fff"/><ellipse cx="13" cy="11" rx="6" ry="4.5" fill="#fff" stroke="#0f3c5b" stroke-width="1.5"/></svg></span></a>
<a href="#" class="cta cta-subscribe"><span>Subscribe to<br>our Newsletter</span>
  <span class="cta-icon"><svg width="14" height="18" viewBox="0 0 14 18"><path d="M1 1h8l4 4v12H1z" fill="#fff"/><path d="M9 1v4h4" fill="none" stroke="#0f3c5b" stroke-width="1.5"/></svg></span></a>

<main class="content">
  <h1>How it works</h1>
  <p>Lorem ipsum dolor sit amet, consectetuer adipiscing elit, sed diam nonummy nibh<br>euismod tincidunt ut laoreet dolore magna aliquam erat volutpat. Ut wisi enim.</p>
  <p>Lorem ipsum dolor sit amet, consectetuer adipiscing elit, sed diam nonummy nibh<br>euismod tincidunt ut laoreet dolore magna aliquam erat volutpat. Ut wisi enim.</p>
  <p>Lorem ipsum dolor sit amet, consectetuer adipiscing elit, sed diam nonummy nibh<br>euismod tincidunt ut laoreet dolore magna aliquam erat volutpat. Ut wisi enim anbv.<br>lo ipsum dolor sit amet, consectetuer adipiscing elit, sed diam nonummy nibh euismod<br>tincidunt ut laoreet dolore magna aliquam erat volutpat. Ut wisi enim nbhtjj.</p>
  <ul class="checklist">
    <li><svg width="16" height="14" viewBox="0 0 16 14"><path d="M1 8l5 5L15 2l-2-1-7 8-3-3z" fill="var(--tick)"/></svg>Lorem ipsum dolor sit amet, consectetuer adipiscing elit.</li>
    <li><svg width="16" height="14" viewBox="0 0 16 14"><path d="M1 8l5 5L15 2l-2-1-7 8-3-3z" fill="var(--tick)"/></svg>Lorem ipsum dolor sit amet, consectetuer adipiscing elit,</li>
    <li><svg width="16" height="14" viewBox="0 0 16 14"><path d="M1 8l5 5L15 2l-2-1-7 8-3-3z" fill="var(--tick)"/></svg>Lorem ipsum dolor sit amet, consectetuer adipiscing elit,</li>
    <li><svg width="16" height="14" viewBox="0 0 16 14"><path d="M1 8l5 5L15 2l-2-1-7 8-3-3z" fill="var(--tick)"/></svg>Lorem ipsum dolor sit amet, consectetuer adipiscing elit,</li>
    <li><svg width="16" height="14" viewBox="0 0 16 14"><path d="M1 8l5 5L15 2l-2-1-7 8-3-3z" fill="var(--tick)"/></svg>Lorem ipsum dolor sit amet, consectetuer adipiscing elit,</li>
  </ul>
  <p>Lorem ipsum dolor sit amet, consectetuer adipiscing elit, sed diam nonummy nibh<br>euismod tincidunt ut laoreet dolore magna aliquam erat volutpat. Ut wisi enim.</p>
  <p>Lorem ipsum dolor sit amet, consectetuer adipiscing elit, sed diam nonummy nibh<br>euismod tincidunt ut laoreet dolore magna aliquam erat volutpat. Ut wisi enim.</p>
  <p>Lorem ipsum dolor sit amet, consectetuer adipiscing elit, sed diam nonummy nibh<br>euismod tincidunt ut laoreet dolore magna aliquam erat volutpat. Ut wisi enim anbv.<br>lo ipsum dolor sit amet, consectetuer adipiscing elit, sed diam nonummy nibh euismod<br>tincidunt ut laoreet dolore magna aliquam erat volutpat. Ut wisi enim nbhtjj.</p>
</main>

<footer class="site-footer">
  <div class="footer-links">
    <a href="#">Privacy</a><span class="sep">|</span><a href="#">Terms of Use</a><span class="sep">|</span><a href="#">Disclaimer</a><span class="sep">|</span><a href="#">Privacy</a><span class="sep">|</span><a href="#">Contact Us</a><br>
    Copyright © 2013&nbsp; TagRoam . All rights reserved.
  </div>
  <a href="#" class="social" aria-label="Social link" style="left:887px;background:var(--social-red)"></a>
  <a href="#" class="social" aria-label="Social link" style="left:930px;background:var(--social-sky)"></a>
  <a href="#" class="social" aria-label="Social link" style="left:973px;background:var(--social-tube)"></a>
  <a href="#" class="social" aria-label="Social link" style="left:1015px;background:var(--social-navy)"></a>
</footer>
</body>
</html>
```